BrightHeron Tourism & Lifestyle Web Design

Mission & Vision: Bright Heron is a newly formed Lifestyle Company focused on giving its clients a high quality design experience in tourism, travel advice, property management and interior design services in the evolving Nicaraguan Market. There is a gap in the market for a company with a more international approach to these services along with an eye for design. The founders feel that with the development of a trusted website to attract potential clients and visitors to Nicaragua they can differentiate the Bright Heron experience from the current competitors operating in the market. With an eye for clean and modern design adapted to the rustic tropical environment of Nicaragua. The founders of this company are very well travelled individuals with a keen sense of style and design. Utilizing their many experiences abroad will be a key to ensuring that they provide a high end experience for those renting houses through them to those house owners requiring design services to bring their properties up to the Bright Heron standard.
Services & Products: “Tourism and Lifestyle” Services – Vacation Home rentals, Property Management, Interior design services targeting the higher end of the Nicaraguan market and the more affluent design conscious traveller.
Brand Essence: Cool, Modern, forward thinking, stylish design, cutting edge design, tropical minimalism, slightly rustic but always with a designer twist, wise but fun, high quality service.
The Name: “Bright Heron” BRIGHT – Knowing, trustworthy, clean, innovative, experienced HERON – fun, cool, young at heart, cheeky. (Plus there are Howler monkeys in pretty much every vacation destination in Nicaragua)
Target Audience: Both males and females with an adventurous spirit and a discerning eye for modern design – a design-conscious traveller. A broad range of ages from perhaps around 25 years to 60 years. These people are young at heart regardless of their age – they are the global glitterati!! Not budget conscious but like to get value for money – very aware of how much things should cost. Are willing to pay extra to stay in a place that is more on par with their ideas of what is good. They like things that are cool and look cool!! Those little touches that make the experience that much nicer. Whilst the audience will be from all around the world the main markets will be the USA, UK, Canada, Germany, Italy, France, Australia, Spain, South America, Mexico.
Competitive Niche: Bright Heron will offer a service that is not available in Nicaragua currently. Focusing on the higher quality and unique properties in the market as well as providing interior design services for existing and new properties. Generally the Vacation rental market tends to overlook those finishing touches that will make a property that much more comfortable and fun to stay in.
Examples to Reference: Bright Heron’s goal is to become the Velour (www.velourstays-example.com ) of Vacation Rentals. What Velour does for hotels we want to do for House and apartment rentals. The idea is to start in Nicaragua and then take on other countries. Bright Heron will also work with Nestora (www.nestora-example.com) listing the properties on their site for more exposure and credibility. Other references would be the Quillmark guides. (www.quillmark-example.com) And Plinth Lodges (www.plinthlodges-example.com)
Competitors and Partners: The Vacation Rental website company: 1) KZLP www.kzlp-example.com 2) Nestora www.nestora-example.com 3) www.lakeshoreholidayhomes-example.com 4) www.holidayhomeslakeshore-example.com 5) www.tovaretreat-example.com 6)www.brisolvante-example.com 7) www.journeyvoter-example.com

Project Deadline Extended
Reason: The project was only launched today as I have been trying to finalise the logo. I should have all the artwork for the logo by tomorrow. I believe this is a simple design so 7 days should be long enough.

The Artwork files and the colour guidelines will now be posted. Please use these colours along with the logo. if you require more complimentry colours please see the colour palette I already attached from Fern.

Target Market(s)

Industry/Entity Type

Property Management

Requirements
Must have
• Clean, Simple design, modern, Use a really good font that is not classic or traditional, Use newly developed logo, White background with a very simply functionality so as to not inhibit speed. Want to always have the logo at the top along with the main menu and the vacation rental home search tab. (See Velour Stays website)www.velour-example.com
Nice to have
• A new way to achieve the look of the Velour Stays Site.
Should not have
• Flash or anything that slows the site down. Permanent photos or pictures as the houses will provide a lot of the pictures and these will need to be updated and changed all the time.

```html
<!DOCTYPE html>
<html lang="en">
<head>
<meta charset="utf-8">
<title>BrightHeron — Tourism &amp; Lifestyle</title>
<link rel="stylesheet" href="https://fonts.googleapis.com/css2?family=Ubuntu:wght@400;500;700&family=Open+Sans:ital,wght@0,400;0,600;1,400&display=swap">
<style>
:root{
  --green:#6a9a2a;
  --green-dark:#4f7a1c;
  --green-light:#8cc63f;
  --text:#333;
  --muted:#777;
  --panel:#3d4036;
  --line:#e3e3e3;
  --footer:#f0f0f0;
}
*{box-sizing:border-box;margin:0;padding:0}
html,body{width:816px;height:1200px;overflow:hidden;background:#fff}
body{position:relative;font-family:"Open Sans",sans-serif;color:var(--text)}
.abs{position:absolute}
.topline{left:0;top:0;width:816px;height:3px;background:var(--green-light)}
.account-btn{top:3px;height:21px;padding:0 12px;background:linear-gradient(#7aa83a,#5e8a24);color:#fff;font:500 11px/21px "Ubuntu",sans-serif;border-radius:0 0 2px 2px}
.brand{left:72px;top:30px;font:700 33px/1 "Ubuntu",sans-serif;color:var(--green);letter-spacing:-0.5px}
.main-nav{left:376px;top:51px;display:flex;font:400 12px/14px "Ubuntu",sans-serif;color:var(--green-dark)}
.main-nav span{padding:0 12px;border-left:1px solid #bbb}
.main-nav span:first-child{border-left:0;padding-left:0}
.hero-band{left:0;top:80px;width:816px;height:220px;background:linear-gradient(#fff,#f1f1f1)}
.hero-frame{left:71px;top:87px;width:674px;height:265px;background:#fff;box-shadow:0 0 4px rgba(0,0,0,.15)}
.hero-photo{left:75px;top:91px;width:666px;height:258px;background:linear-gradient(180deg,#cfe4f0 0%,#a9c7d4 40%,#7e9a6a 70%,#4f6a3a 100%)}
.hero-arrows{left:88px;top:318px;color:#fff;font:700 20px/1 "Ubuntu",sans-serif}
.search-panel{left:523px;top:96px;width:214px;height:245px;background:var(--panel);padding:18px 19px}
.search-panel h2{font:500 19px/22px "Ubuntu",sans-serif;color:#fff;margin-bottom:10px}
.field-label{font:400 9px/1 "Ubuntu",sans-serif;color:var(--green-light);margin-bottom:4px}
.field{height:20px;background:#fff;border:1px solid #ccc;font-size:7.5px;line-height:18px;padding-left:8px;color:#666;position:relative;margin-bottom:10px}
.field .cal{position:absolute;right:5px;top:5px;width:11px;height:9px;border:1px solid #999;border-top-width:2px}
.pair{display:flex;gap:4px}
.pair>div{flex:1}
.search-btn{height:25px;margin-top:1px;background:linear-gradient(#8cc63f,#6aa52a);color:#fff;text-align:center;font:500 10.5px/25px "Ubuntu",sans-serif;letter-spacing:.2px}
.section-title{font:500 18px/1 "Ubuntu",sans-serif;color:#333}
.intro{left:78px;top:398px;width:540px;font-size:8.5px;line-height:16px;color:var(--muted)}
.card{width:157px;height:128px;background:#fff;border:1px solid #ddd;box-shadow:0 1px 2px rgba(0,0,0,.08)}
.card .photo{height:99px}
.card .name{position:absolute;left:13px;top:104px;font:500 12.5px/1 "Ubuntu",sans-serif;color:var(--green-dark)}
.card .view{position:absolute;right:9px;top:104px;height:17px;padding:0 6px;border:1px solid #ddd;background:linear-gradient(#fff,#f0f0f0);font-size:7px;line-height:15px;color:#666}
.divider{height:1px;background:var(--line)}
.video{left:79px;top:774px;width:204px;height:138px;background:#3a3a3a;padding:4px}
.video .photo{width:100%;height:100%;background:linear-gradient(135deg,#d9d2c4,#b9c8d8 50%,#c98a7a)}
.play{left:168px;top:827px;width:28px;height:28px;border-radius:50%;background:#222;border:2px solid #fff}
.play:after{content:"";position:absolute;left:10px;top:7px;border-left:9px solid #fff;border-top:5.5px solid transparent;border-bottom:5.5px solid transparent}
.info h3{font:400 17px/1 "Ubuntu",sans-serif;color:#333;margin-bottom:10px}
.info h4{font:400 10px/1 "Ubuntu",sans-serif;color:#444;margin-bottom:11px}
.info p{font-size:8.3px;line-height:16px;color:var(--muted);margin-bottom:9px;white-space:nowrap}
.learn{display:inline-block;height:20px;padding:0 10px;background:linear-gradient(#6f9d33,#4d7a1d);color:#fff;font:400 8px/20px "Ubuntu",sans-serif}
.footer{left:0;top:946px;width:816px;height:254px;background:var(--footer);border-top:1px solid #e6e6e6}
.foot-col h5{font:400 13px/1 "Ubuntu",sans-serif;color:#444;margin-bottom:9px}
.foot-col li{list-style:none;font-size:8.5px;line-height:19px;color:#555;padding-left:2px}
.newsletter p{font-size:8.5px;color:#555;margin-bottom:8px;padding-left:2px}
.email{width:170px;height:22px;background:#fff;border:1px solid #ccc;font:italic 8px/20px "Open Sans",sans-serif;color:#888;padding-left:9px;position:relative;margin-left:2px}
.email:after{content:"";position:absolute;right:8px;top:5px;border-left:7px solid #333;border-top:5px solid transparent;border-bottom:5px solid transparent}
.follow{display:flex;align-items:center;gap:3px;margin-top:10px;font-size:8.5px;color:#555;padding-left:3px}
.follow span{margin-right:3px}
.follow i{display:block;width:19px;height:19px;border-radius:50%;background:#111}
.copyright{left:74px;top:1153px;font-size:8.5px;color:#777}
</style>
</head>
<body>
<div class="abs topline"></div>
<div class="abs account-btn" style="left:618px">Sign Up</div>
<div class="abs account-btn" style="left:681px">Login</div>
<div class="abs brand">BrightHeron</div>
<nav class="abs main-nav"><span>Main</span><span>About Us</span><span>Services</span><span>Tours</span><span>Book Now</span><span>Contact</span></nav>

<div class="abs hero-band"></div>
<div class="abs hero-frame"></div>
<div class="abs hero-photo" role="img" aria-label="Two hikers with backpacks on a rocky summit overlooking misty green mountains"></div>
<div class="abs hero-arrows">&lsaquo;&rsaquo;</div>
<form class="abs search-panel">
  <h2>Find Your Dream Destination</h2>
  <div class="field-label">Destination</div>
  <div class="field">enter your location/tour</div>
  <div class="pair">
    <div><div class="field-label">Check In</div><div class="field">Arriving date<span class="cal"></span></div></div>
    <div><div class="field-label">Check Out</div><div class="field">Leaving date<span class="cal"></span></div></div>
  </div>
  <div class="pair">
    <div><div class="field-label">No. of Adults</div><div class="field">5 Adults</div></div>
    <div><div class="field-label">No. of Childrens</div><div class="field">10 Children</div></div>
  </div>
  <div class="search-btn">SEARCH TOUR NOW</div>
</form>

<h2 class="abs section-title" style="left:78px;top:377px">Best Destinations</h2>
<p class="abs intro">Duis tincidunt lectus quis dui viverra vestibulum. Suspendisse vulputate aliquam dui. Nulla elementum dui ut augue. Aliquam vehicula mi at mauris. Maecenas placerat, nisl at consequat rhoncus, sem nunc gravida justo</p>

<div class="abs card" style="left:76px;top:445px"><div class="photo" role="img" aria-label="Palm-lined beach and pier in Los Angeles" style="background:linear-gradient(#6fa6d8,#a9cde6 55%,#d9c9a8)"></div><span class="name">Los Angeles</span><span class="view">View Tours ›</span></div>
<div class="abs card" style="left:244px;top:445px"><div class="photo" role="img" aria-label="Capitol building and monument in Austin" style="background:linear-gradient(#2f6fc0,#9cc2e4 55%,#b9b7a7 75%,#5f7f3a)"></div><span class="name">Austin</span><span class="view">View Tours ›</span></div>
<div class="abs card" style="left:412px;top:445px"><div class="photo" role="img" aria-label="Boston downtown skyline from above" style="background:linear-gradient(#7fb0e0,#8b8e95 45%,#5d6168)"></div><span class="name">Boston</span><span class="view">View Tours ›</span></div>
<div class="abs card" style="left:580px;top:445px"><div class="photo" role="img" aria-label="Roman Forum ruins and church dome in Rome" style="background:linear-gradient(#9cc3e6,#c99c6a 50%,#8b5e36)"></div><span class="name">Rome</span><span class="view">View Tours ›</span></div>

<div class="abs card" style="left:76px;top:587px"><div class="photo" role="img" aria-label="Basilica domes in Venice under blue sky" style="background:linear-gradient(#4c86c6,#a9c6e0 50%,#a89a86)"></div><span class="name">Venice</span><span class="view">View Tours ›</span></div>
<div class="abs card" style="left:244px;top:587px"><div class="photo" role="img" aria-label="Berlin riverside skyline with clouds" style="background:linear-gradient(#3f7fc8,#dfe9f2 45%,#8a7a6a 75%,#4b6a86)"></div><span class="name">Berlin</span><span class="view">View Tours ›</span></div>
<div class="abs card" style="left:412px;top:587px"><div class="photo" role="img" aria-label="Eiffel Tower above green gardens in Paris" style="background:linear-gradient(#2e6cc0,#d8e6f2 50%,#6f8f3a 85%)"></div><span class="name">Paris</span><span class="view">View Tours ›</span></div>
<div class="abs card" style="left:580px;top:587px"><div class="photo" role="img" aria-label="Tower Bridge over the Thames in London" style="background:linear-gradient(#5d92cf,#b8cde0 45%,#9a8d78 80%,#6a6f66)"></div><span class="name">London</span><span class="view">View Tours ›</span></div>

<div class="abs divider" style="left:76px;top:745px;width:672px"></div>

<div class="abs video"><div class="photo" role="img" aria-label="Smiling travelling couple reading a guidebook in a colonial town square"></div></div>
<div class="abs play"></div>
<div class="abs info" style="left:311px;top:775px;width:210px">
  <h3>Services &amp; Products</h3>
  <h4>Tourism and Lifestyle Services</h4>
  <p>Vacation Home rentals, Property Management,<br>Interior design services targeting the higher end<br>of the Nicaraguan market and the more affluent<br>design conscious traveller.</p>
  <span class="learn">Learn More ▸</span>
</div>
<div class="abs info" style="left:537px;top:775px;width:210px">
  <h3>Our Trust &amp; Safety</h3>
  <h4>Duis tincidunt lectus quis dui</h4>
  <p>Viverra vestibulum. Suspendisse vulputate<br>aliquam dui. Nulla elementum dui ut augue. Ali-<br>quam vehicula mi at mauris. Maecenas placerat,<br>nisl at consequat rhoncus sem nunc justo</p>
  <span class="learn">Learn More ▸</span>
</div>

<footer class="abs footer"></footer>
<div class="abs foot-col" style="left:85px;top:980px"><h5>Company</h5><ul><li>Home</li><li>About Us</li><li>Our Travel</li><li>Top Destination</li><li>What We Offers</li></ul></div>
<div class="abs foot-col" style="left:200px;top:980px"><h5>Popular Destination</h5><ul><li>Nunc tempus</li><li>Felis vitae urna</li><li>Vivamus porttitor</li><li>Purus nisi eleifend</li><li>Tempus libero lectus</li></ul></div>
<div class="abs foot-col" style="left:356px;top:980px"><h5>Support</h5><ul><li>FAQ</li><li>Testimonials</li><li>Blog Post</li><li>Customer Help</li><li>Contact Info</li></ul></div>
<div class="abs foot-col newsletter" style="left:469px;top:980px">
  <h5>Sign Up Newsletters</h5>
  <p>Please sign up here for latest newsletters</p>
  <div class="email">email address</div>
  <div class="follow"><span>Follow Us With</span><i></i><i></i><i></i><i></i></div>
</div>
<div class="abs divider" style="left:72px;top:1138px;width:672px;background:#ddd"></div>
<div class="abs copyright">© 2013 Company Name.&nbsp; All right reserved.&nbsp; Term of Use</div>
</body>
</html>
```